Velora, Pure Glow label sticker for cosmetic cream

I'm looking to design a label sticker for my cosmetic brand. The product is called Pure Glow. The brand is called Velora. I'm looking for a minimalistic, modern design that encapsulates the fact that the product is all natural. Made with 100% organic ingredients, vegan and cruelty free. The motto of the company is " The Healing Power of Nature"

Target Market(s)

Young professionals, 30+, 40+ interested in natural skin care

Industry/Entity Type

Cosmetic

Colors

Designer to choose only greyscale colors for use in the design.

Requirements
Must have
• Modern look, easily remembered but still a touch of nature

```html
<!DOCTYPE html>
<html lang="en">
<head>
<meta charset="utf-8">
<title>Velora – Pure Glow Label</title>
<link rel="stylesheet" href="https://fonts.googleapis.com/css2?family=Montserrat:wght@300;400;500;700&display=swap">
<style>
  :root {
    --paper: #ffffff;
    --ink: #111111;
    --ink-soft: #333333;
    --rule: #222222;
  }
  * { margin: 0; padding: 0; box-sizing: border-box; }
  html, body {
    width: 1200px; height: 636px; overflow: hidden;
    background: var(--paper);
    font-family: "Montserrat", Arial, sans-serif;
    color: var(--ink);
  }
  .label { position: relative; width: 1200px; height: 636px; background: var(--paper); overflow: hidden; }

  /* Side panel */
  .directions { position: absolute; left: 77px; top: 154px; width: 184px; }
  .directions-title { font-size: 19px; font-weight: 400; }
  .directions-title small { font-size: 6px; font-weight: 500; vertical-align: middle; }
  .directions-text {
    margin-top: 12px; font-size: 15.5px; line-height: 22.5px;
    text-align: justify; font-weight: 500; color: var(--ink-soft);
  }
  .contacts { position: absolute; left: 80px; top: 426px; list-style: none; }
  .contacts li { display: flex; align-items: center; height: 27.5px; font-size: 12px; font-weight: 500; }
  .contacts svg { width: 14px; height: 14px; margin-right: 9px; flex: none; }

  /* Main panel */
  .main {
    position: absolute; left: 312px; width: 800px;
    text-align: center; white-space: nowrap; line-height: 1;
  }
  .brand { top: 80px; font-size: 46px; font-weight: 400; letter-spacing: 0.28em; padding-left: 0.28em; }
  .product { top: 200px; font-size: 82px; font-weight: 700; letter-spacing: 0.16em; padding-left: 0.16em; }
  .tagline { top: 310px; font-size: 26px; font-weight: 400; letter-spacing: 0.11em; padding-left: 0.11em; }
  .divider { position: absolute; left: 592px; top: 392px; width: 234px; height: 2px; background: var(--rule); }
  .claims { position: absolute; top: 449px; left: 399px; font-size: 20px; font-weight: 400; letter-spacing: 0.04em; line-height: 1; }
  .claims span { position: absolute; white-space: nowrap; }
  .claims .sep { left: 308px; }
  .claims .organic { left: 389px; }
  .volume { top: 550px; font-size: 21px; font-weight: 400; letter-spacing: 0.04em; }
</style>
</head>
<body>
<main class="label">
  <section class="directions">
    <h2 class="directions-title">Direction : <small>(Editable)</small></h2>
    <p class="directions-text">Lorem ipsum dolor sit amet, consectetuer adipiscing elit, sed diam nonummy nibh euismod tincidunt ut laoreet dolore magna aliquam. Lorem ipsum dolor sit amet.</p>
  </section>

  <ul class="contacts">
    <li><svg viewBox="0 0 14 14"><rect x="1" y="1" width="12" height="12" fill="var(--ink)"/></svg>@veloracosmetics</li>
    <li><svg viewBox="0 0 14 14"><circle cx="7" cy="7" r="6" fill="var(--ink)"/></svg>@veloracosmetics</li>
    <li><svg viewBox="0 0 14 14" fill="none" stroke="var(--ink)" stroke-width="1.4"><circle cx="7" cy="7" r="6"/><ellipse cx="7" cy="7" rx="2.6" ry="6"/><line x1="1" y1="7" x2="13" y2="7"/></svg>www.veloracosmetics.com</li>
  </ul>

  <h1 class="main brand">VELORA</h1>
  <p class="main product">PURE GLOW</p>
  <p class="main tagline">THE HEALING POWER OF NATURE</p>
  <div class="divider"></div>
  <p class="claims">
    <span>HANDMADE IN USA</span>
    <span class="sep">|</span>
    <span class="organic">100% ORGANIC</span>
  </p>
  <p class="main volume">8 oz / 240 ml</p>
</main>
</body>
</html>
```